Logo for a recruitment consultancy and executive search firm
The Ashcombe Reeve Partnership
Logo for a recruitment consultancy and executive search firm - Consulting
Creative Brief
Professional
Marian Colbeck
Head of Practice
London office: Belgrove Court 42 Belgrove Court Mayfair London W1K 4PL Dublin office: Block C The Larchfield House Oakpark, Kilbarrow Dublin, 9
marian@ashcombe-reeve.example
www.ashcombe-reeve.example
We will need 3 other business cards details are as follows: Name: Tarek Haddadi Title: Head of Practice Address: London office: Belgrove Court 42 Belgrove Court Mayfair London W1K 4PL Dublin office: Block C The Larchfield House Oakpark, Kilbarrow Dublin, 9 Phone: 020 7946 0321 Mobile: 07700900482 Email: tarek@ashcombe-reeve.example Name: Judith Purcell Title: CEO Address: London office: Belgrove Court 42 Belgrove Court Mayfair London W1K 4PL Dublin office: Block C The Larchfield House Oakpark, Kilbarrow Dublin, 9 Phone: 020 7946 0321 Mobile: 07700 900 615 Email: judith@ashcombe-reeve.example Name: Helen Varty Title: Finance Manager Address: London office: Belgrove Court 42 Belgrove Court Mayfair London W1K 4PL Dublin office: Block C The Larchfield House Oakpark, Kilbarrow Dublin, 9 0321 Mobile: 07700 900 738 email: accounts@ashcombe-reeve.example We want the complete stationary set! The more the merrier as far as I am concerned. folders compliment strips headed paper email signature envelopes presentation format position documents folder you name it we want it!
Black with Ashcombe reeve logo

```html
<!DOCTYPE html>
<html lang="en">
<head>
<meta charset="utf-8">
<title>The Ashcombe Reeve Partnership — Business Card</title>
<link href="https://fonts.googleapis.com/css2?family=Cinzel:wght@400;600&display=swap" rel="stylesheet">
<style>
  :root {
    --page-bg: #e9e7e4;
    --ink: #231f20;
    --paper: #ffffff;
    --stripe-light: #c9c9c9;
    --stripe-mid: #8c8c8c;
    --text-dark: #2b2b2b;
    --text-light: #ffffff;
  }
  * { margin: 0; padding: 0; box-sizing: border-box; }
  html, body {
    width: 1200px; height: 900px; overflow: hidden;
    background: var(--page-bg);
    font-family: "Cinzel", serif;
  }
  .card {
    position: absolute; left: 100px; top: 165px;
    width: 1000px; height: 570px;
    background: var(--paper);
    overflow: hidden;
    box-shadow: 0 10px 30px rgba(0,0,0,.18);
  }
  .card__band {
    position: absolute; left: 0; top: 0; width: 100%; height: 255px;
    background: var(--ink);
  }
  .card__notch { position: absolute; left: 70px; top: 254px; }
  .card__accent {
    position: absolute; left: 150px; top: 255px; right: 0; height: 14px;
    background: var(--stripe-light);
  }
  .card__footer {
    position: absolute; left: 0; bottom: 0; width: 100%; height: 70px;
    background: linear-gradient(var(--stripe-light) 0 18px, var(--stripe-mid) 18px);
  }
  .brand {
    position: absolute; left: 0; top: 62px; width: 100%;
    text-align: center; color: var(--text-light);
  }
  .brand__mark {
    display: block; width: 54px; height: 54px; margin: 0 auto 22px;
    border-radius: 50%; background: var(--text-light);
  }
  .brand__name {
    font-weight: 400; font-size: 34px; letter-spacing: 1px; line-height: 1.1;
  }
  .brand__sub {
    display: flex; align-items: center; justify-content: center; gap: 12px;
    font-weight: 400; font-size: 15px; letter-spacing: 2px; margin-top: 4px;
  }
  .brand__sub::before, .brand__sub::after {
    content: ""; width: 90px; border-top: 1px dotted var(--text-light);
  }
  .person {
    position: absolute; left: 58px; top: 300px; color: var(--text-dark);
  }
  .person__name { font-size: 30px; font-weight: 400; }
  .person__title { font-size: 19px; margin-top: 6px; }
  .contacts {
    position: absolute; left: 560px; top: 296px; list-style: none;
    color: var(--text-dark); font-size: 16px; line-height: 1.25;
  }
  .contacts li { display: flex; align-items: flex-start; gap: 10px; margin-bottom: 5px; }
  .contacts svg { flex: none; width: 20px; height: 20px; }
</style>
</head>
<body>
  <article class="card">
    <div class="card__band"></div>
    <svg class="card__notch" width="36" height="20" viewBox="0 0 36 20"><polygon points="0,0 36,0 18,20" fill="var(--ink)"/></svg>
    <div class="card__accent"></div>
    <div class="card__footer"></div>

    <header class="brand">
      <span class="brand__mark"></span>
      <div class="brand__name">ASHCOMBE REEVE</div>
      <div class="brand__sub">PARTNERSHIP</div>
    </header>

    <section class="person">
      <h1 class="person__name">Marian Colbeck</h1>
      <p class="person__title">Head of Practice</p>
    </section>

    <ul class="contacts">
      <li>
        <svg viewBox="0 0 20 20"><circle cx="10" cy="10" r="10" fill="var(--ink)"/><path d="M10 4a4 4 0 0 0-4 4c0 3 4 8 4 8s4-5 4-8a4 4 0 0 0-4-4z" fill="#fff"/><circle cx="10" cy="8" r="1.5" fill="var(--ink)"/></svg>
        <span>Block C The Larchfield House<br>Oakpark, Kilbarrow Dublin, 9</span>
      </li>
      <li>
        <svg viewBox="0 0 20 20"><circle cx="10" cy="10" r="10" fill="var(--ink)"/><path d="M6.5 5h2l1 2.5-1.3 1a6 6 0 0 0 3.3 3.3l1-1.3 2.5 1v2a1 1 0 0 1-1 1A9 9 0 0 1 5.5 6a1 1 0 0 1 1-1z" fill="#fff"/></svg>
        <span>020 7946 0321</span>
      </li>
      <li>
        <svg viewBox="0 0 20 20"><circle cx="10" cy="10" r="10" fill="var(--ink)"/><rect x="7" y="4" width="6" height="12" rx="1" fill="#fff"/><rect x="8" y="5.5" width="4" height="7.5" fill="var(--ink)"/></svg>
        <span>07700 900 482</span>
      </li>
      <li>
        <svg viewBox="0 0 20 20"><circle cx="10" cy="10" r="10" fill="var(--ink)"/><rect x="5" y="6.5" width="10" height="7" fill="#fff"/><path d="M5 6.5l5 4 5-4" fill="none" stroke="var(--ink)" stroke-width="1"/></svg>
        <span>marian@ashcombe-reeve.example</span>
      </li>
      <li>
        <svg viewBox="0 0 20 20"><circle cx="10" cy="10" r="10" fill="var(--ink)"/><circle cx="10" cy="10" r="5" fill="none" stroke="#fff" stroke-width="1.2"/><path d="M5 10h10M10 5c-2.5 3-2.5 7 0 10M10 5c2.5 3 2.5 7 0 10" fill="none" stroke="#fff" stroke-width="1"/></svg>
        <span>www.ashcombe-reeve.example</span>
      </li>
    </ul>
  </article>
</body>
</html>
```